Veromar Cargo Flower trade show brochure

We are an international freight forwarding company from South America specialising in perishable handling both through air freight and sea freight. We need a brochure to hand out to customers in the flower fair trade shows in which we participate - China, Holland, Russia, USA. We need something clean yet striking and modern emphasising our brand and with great emphasis on our strengths in the perishable/flower forwarding realm. Our company is a merger of 4 of the largest forwarders in Ecuador into one company called Veromar Cargo Group. We would like emphasis on the new brand, however we do require that each individual logo of the 4 companies is portrayed in some way in the brochure. We are also registered with a global freight forwarding association known as PNQ which also must be mentioned. We would like a defined concept for perishable handling, something along the lines of (but not limited to) - first class travel - dont your flowers deserve the same ? Attached a JPEG file with our new website proposed design so that you have an idea of our tastes. Also attached is some basic text which can be used to put together the brochure. We would like some emphasis also on some fast data facts such as - 1. We ship to over 80 countries worldwide 2. we forward over 5000 tons of flowers per month 3. we track and trace over 150 shipments per day etc etc. Please also include our website adress - www.veromarcargo, and something along the lines of - Follow us on (logo Connectry), (logo Friendloop), logo (chirpnet) and our contact email address - info@veromarcargo.example

Target Market(s)

Flower importers worldwide

Industry/Entity Type

Freight Forwarding

Font styles to use
Sans Serif

Colors
9bcb3b
acd036
9d9d9d
757575

Requirements
Must have
• Photos of freight forwarding concepts, cut flowers

```html
<!DOCTYPE html>
<html lang="en">
<head>
<meta charset="utf-8">
<title>Veromar Cargo – Flower Trade Show Brochure</title>
<link rel="stylesheet" href="https://fonts.googleapis.com/css2?family=Open+Sans:wght@400;600;700;800&display=swap">
<style>
  :root {
    --stage: #3f3f3f;
    --paper: #ffffff;
    --green: #9bcb3b;
    --green-light: #acd036;
    --grey: #9d9d9d;
    --grey-dark: #757575;
    --ink: #1a1a1a;
  }
  * { box-sizing: border-box; margin: 0; padding: 0; }
  html, body { width: 937px; height: 1200px; overflow: hidden; }
  body {
    background: var(--stage);
    font-family: "Open Sans", Arial, sans-serif;
    position: relative;
  }
  .brochure {
    position: absolute;
    left: 34px; top: 290px;
    width: 870px; height: 620px;
    display: flex;
  }
  .panel {
    width: 290px; height: 100%;
    background: var(--paper);
    position: relative;
  }
  .panel + .panel { border-left: 1px solid #e4e4e4; }

  /* Facts panel */
  .panel--facts { overflow: hidden; }
  .facts-photo {
    position: absolute; inset: 0;
    background: linear-gradient(160deg, #f2f2f2 0%, #d6d6d8 35%, #b9b9bd 70%, #a6a6ab 100%);
  }
  .facts-list {
    position: absolute; left: 95px; top: 120px;
    display: flex; flex-direction: column; gap: 14px;
  }
  .fact {
    width: 118px;
    background: var(--paper);
    border: 2px dashed var(--green);
    border-radius: 12px;
    padding: 8px 6px 9px;
    text-align: center;
    color: var(--grey-dark);
    font-size: 12px; line-height: 1.1;
  }
  .fact__number {
    display: block;
    color: var(--green);
    font-weight: 800;
    font-size: 38px; line-height: 1;
  }
  .fact__unit { color: var(--green); display: block; }

  /* Back cover panel */
  .panel--back { display: flex; flex-direction: column; align-items: center; }
  .brand {
    display: flex; align-items: center; gap: 8px;
    font-weight: 700; color: var(--grey-dark);
    white-space: nowrap;
  }
  .brand__mark { width: 16px; height: 16px; border-radius: 50%; background: var(--green); flex: none; }
  .brand__group {
    font-size: 7px; letter-spacing: 3px; color: var(--grey);
    text-align: center; margin-top: 2px;
  }
  .panel--back .brand-block { margin-top: 200px; }
  .panel--back .brand { font-size: 19px; }
  .follow {
    margin-top: 190px;
    display: flex; gap: 10px;
    font-size: 10px; font-weight: 600; color: var(--green);
    white-space: nowrap;
  }
  .contact {
    margin-top: 34px; text-align: center;
    font-size: 10px; line-height: 1.5;
    white-space: nowrap;
  }
  .contact__email { color: var(--grey-dark); }
  .contact__web { color: var(--green); font-weight: 600; }

  /* Front cover panel */
  .panel--cover { display: flex; flex-direction: column; align-items: center; }
  .panel--cover .brand-block { margin-top: 58px; }
  .panel--cover .brand { font-size: 20px; }
  .cover-rule { width: 230px; height: 1px; background: #dcdcdc; margin-top: 18px; }
  .photo-plane {
    margin-top: 26px; width: 170px; height: 40px;
    background: radial-gradient(ellipse at center, #c9c9cc 0%, #e9e9ea 55%, var(--paper) 100%);
  }
  .photo-flowers {
    margin-top: 22px; width: 230px; height: 160px;
    background: radial-gradient(ellipse at 45% 45%, #e07aa8 0%, #f2b6d0 45%, #f7e4ec 70%, var(--paper) 100%);
  }
  .tagline { margin-top: 34px; text-align: center; color: var(--ink); white-space: nowrap; }
  .tagline__title { font-size: 19px; font-weight: 800; letter-spacing: 0.2px; }
  .tagline__sub { font-size: 8.5px; font-weight: 600; }
</style>
</head>
<body>
  <main class="brochure">
    <section class="panel panel--facts">
      <div class="facts-photo" role="img" aria-label="Stacked shipping containers photo in soft greys"></div>
      <div class="facts-list">
        <div class="fact">We ship to over<span class="fact__number">80</span><span class="fact__unit">countries</span>worldwide</div>
        <div class="fact">we forward over<span class="fact__number">5000</span><span class="fact__unit">tons</span>of flowers<br>per month</div>
        <div class="fact">we track and<br>trace over<span class="fact__number">150</span><span class="fact__unit">shipments</span>per day</div>
      </div>
    </section>

    <section class="panel panel--back">
      <div class="brand-block">
        <div class="brand"><span class="brand__mark"></span>Veromar Cargo</div>
        <div class="brand__group">GROUP</div>
      </div>
      <div class="follow">
        <span>Friendloop</span><span>chirpnet</span><span>Connectry</span>
      </div>
      <div class="contact">
        <div class="contact__email">info@veromarcargo.example</div>
        <div class="contact__web">www.veromarcargo.example</div>
      </div>
    </section>

    <section class="panel panel--cover">
      <div class="brand-block">
        <div class="brand"><span class="brand__mark"></span>Veromar Cargo</div>
        <div class="brand__group">GROUP</div>
      </div>
      <div class="cover-rule"></div>
      <div class="photo-plane" role="img" aria-label="Cargo airplane in flight"></div>
      <div class="photo-flowers" role="img" aria-label="Branch of pink dogwood flowers"></div>
      <div class="tagline">
        <div class="tagline__title">FIRST CLASS TRAVEL</div>
        <div class="tagline__sub">DONT YOUR FLOWERS DESERVE THE SAME ?</div>
      </div>
    </section>
  </main>
</body>
</html>
```